Visual design for database driven web application

Need a clean, professional looking visual design for a web application.

PLUME is the new standardized K-12 school testing program for the state of Texas. We are building an application named PLUME-Finder (clever, yeah?) that will allow teachers, school administrators, and others to EASILY sort through millions of records of student data and print or export reports showing just the information they need about their students.

The state currently doesn't provide a user-friendly way to do this. They provide a "data dump" spreadsheet that school administrators and teachers must figure out how to manipulate to get the data they need. We are building a Web-based tool that will make it super simple and easy for our users to get the data they need in a format that works for them.

I've created a basic wireframe of the main application screen in Vellum QD Max. I need you to "skin" the wireframe to make it look good. Your mockup will set the tone for branding and visual design throughout the site.

See the attached screenshots. There are a few variations of the screen that include dynamic panels that open & close. Start by designing just the main screen and if you have time, do one or two of the panels. Thanks!
Updates

Target Market(s)

K-12 education professionals (teachers, administrators) in the state of Texas

Industry/Entity Type

Building

Requirements
Must have
• Your mockups should include all of the features & content shown in the attached screenshots.

However, you don't have to show all 10 rows of data. You can just do the column headers and one row of data. (It would be repetitive and unnecessary to spend time re-creating the entire grid with all of that data just to show your visual styling.)

The design should reflect the following concepts:

- Texas
- Education
- Simplicity
- Helpfulness
- Trust
- Professionalism

If I select your design, I will want your design source files (Illustrator, Photoshop, etc.)
Nice to have
• A logo in the upper left corner for PLUME-Finder. The logo should definitely communicate the design concepts described under "must have."

```html
<!DOCTYPE html>
<html lang="en">
<head>
<meta charset="utf-8">
<title>PLUME-Finder · Student Data</title>
<link rel="stylesheet" href="https://fonts.googleapis.com/css2?family=Arimo:wght@400;700&display=swap">
<style>
  :root {
    --navy-top: #0b0f86;
    --navy-bottom: #0a1aa3;
    --brand-red: #c8102e;
    --brand-red-dark: #a80d26;
    --ink: #444444;
    --ink-soft: #555555;
    --line: #d4d4d4;
    --row-alt: #f0f0f0;
    --panel-top: #ffffff;
    --panel-bottom: #f2f2f2;
    --white: #ffffff;
    --page-active: #666666;
  }
  * { box-sizing: border-box; margin: 0; padding: 0; }
  html, body { width: 1200px; height: 751px; overflow: hidden; background: var(--white); }
  body { font-family: "Arimo", Arial, sans-serif; color: var(--ink); position: relative; }

  .site-header {
    position: absolute; left: 0; top: 0; width: 1200px; height: 112px;
    background: linear-gradient(180deg, var(--navy-top), var(--navy-bottom));
    border-bottom: 4px solid var(--brand-red);
  }
  .brand {
    position: absolute; left: 44px; top: 24px;
    font-size: 29px; font-weight: 400; color: var(--white); letter-spacing: 0.2px;
  }
  .user-nav {
    position: absolute; left: 473px; top: 44px; display: flex; gap: 24px;
    font-size: 15px; color: var(--white);
  }
  .search {
    position: absolute; left: 814px; top: 37px; width: 350px; height: 32px;
    border: 2px solid var(--brand-red); border-radius: 4px; display: flex; overflow: hidden;
    background: var(--white);
  }
  .search-input { flex: 1; border: 0; background: var(--white); }
  .search-button {
    width: 94px; background: var(--brand-red); color: var(--white);
    font-size: 16px; display: flex; align-items: center; justify-content: center;
  }
  .search-options {
    position: absolute; left: 962px; top: 75px; font-size: 14px; color: var(--white);
    display: flex; align-items: center; gap: 5px;
  }
  .search-options span { text-decoration: underline; }
  .tabs { position: absolute; left: 46px; top: 79px; display: flex; align-items: flex-end; height: 29px; }
  .tab { font-size: 15px; color: var(--white); padding: 0 0 8px; }
  .tab.is-active {
    margin-left: 12px; background: var(--brand-red); font-weight: 700;
    padding: 7px 16px 6px; border-radius: 4px 4px 0 0;
  }

  .data-panel {
    position: absolute; left: 18px; top: 131px; width: 1157px; height: 503px;
    border: 1px solid var(--line); border-radius: 6px; overflow: hidden;
    background: linear-gradient(180deg, var(--panel-top), var(--panel-bottom));
  }
  .toolbar { position: absolute; left: 27px; top: 7px; display: flex; align-items: center; font-size: 15px; color: var(--ink-soft); }
  .column-toggle {
    margin: 0 28px 0 24px; height: 33px; padding: 0 16px; border: 1px solid #cfcfcf;
    border-radius: 5px; background: var(--white); display: flex; align-items: center; gap: 10px;
  }
  .filtered { text-decoration: underline; }

  .pager-row { position: absolute; left: 26px; display: flex; align-items: center; font-size: 15px; color: var(--ink-soft); }
  .pager-row.top { top: 55px; }
  .pager-row.bottom { top: 459px; }
  .pager { display: flex; gap: 6px; align-items: center; width: 436px; }
  .page {
    width: 27px; height: 27px; border: 1px solid #c4c4c4; border-radius: 4px;
    background: linear-gradient(180deg, #ffffff, #ececec);
    font-size: 12px; display: flex; align-items: center; justify-content: center; color: #555;
  }
  .page.is-current { background: var(--page-active); color: var(--white); border-color: #555; font-weight: 700; }
  .ellipsis { width: 24px; text-align: center; font-size: 13px; }
  .rows-select {
    margin: 0 8px 0 5px; width: 49px; height: 26px; border: 1px solid #c4c4c4; border-radius: 4px;
    background: var(--white); display: flex; align-items: center; justify-content: space-between; padding: 0 5px;
  }
  .export { position: absolute; right: 22px; top: 59px; display: flex; gap: 20px; font-size: 15px; color: var(--ink-soft); }
  .export span { display: flex; align-items: center; gap: 7px; }

  .student-table {
    position: absolute; left: -1px; top: 94px; width: 1157px;
    border-collapse: collapse; table-layout: fixed; font-size: 14px;
  }
  .student-table th {
    background: var(--brand-red); color: var(--white); font-weight: 400;
    height: 31px; text-align: left; padding-left: 11px;
  }
  .student-table td {
    height: 32.2px; padding-left: 10px; border-left: 1px solid var(--line);
    border-bottom: 1px solid var(--line); background: var(--white); white-space: nowrap;
  }
  .student-table tr:nth-child(even) td { background: var(--row-alt); }
  .student-table td.center { padding-left: 21px; }
</style>
</head>
<body>
  <header class="site-header">
    <div class="brand">PLUME-Finder</div>
    <nav class="user-nav"><span>Welcome, Jack</span><span>|</span><span>My profile</span><span>|</span><span>Logout</span></nav>
    <div class="search"><div class="search-input"></div><div class="search-button">Search</div></div>
    <div class="search-options">
      <svg width="6" height="8" viewBox="0 0 6 8"><path d="M6 0 0 4l6 4z" fill="#fff"/></svg>
      <span>search options</span>
    </div>
    <nav class="tabs"><span class="tab">Instructions</span><span class="tab is-active">Student Data</span></nav>
  </header>

  <main class="data-panel">
    <div class="toolbar">
      <span>Showing 26 of 38 columns</span>
      <span class="column-toggle">
        <svg width="10" height="12" viewBox="0 0 10 12"><path d="M0 0l10 6-10 6z" fill="#111"/></svg>
        Show / Hide columns
      </span>
      <span>3 columns are <span class="filtered">filtered</span></span>
    </div>

    <div class="pager-row top">
      <div class="pager">
        <span class="page"><svg width="7" height="10" viewBox="0 0 7 10"><path d="M6 1 2 5l4 4" stroke="#444" stroke-width="1.6" fill="none"/></svg></span>
        <span class="page">1</span><span class="page">2</span><span class="page">3</span>
        <span class="page is-current">4</span><span class="page">5</span>
        <span class="ellipsis">...</span>
        <span class="page">10</span><span class="page">20</span><span class="page">30</span>
        <span class="page"><svg width="7" height="10" viewBox="0 0 7 10"><path d="M1 1l4 4-4 4" stroke="#444" stroke-width="1.6" fill="none"/></svg></span>
      </div>
      <span>Show</span>
      <span class="rows-select">10<svg width="9" height="6" viewBox="0 0 9 6"><path d="M1 1l3.5 3.5L8 1" stroke="#555" stroke-width="1.5" fill="none"/></svg></span>
      <span>rows &nbsp;per page</span>
    </div>

    <div class="export">
      <span><svg width="20" height="17" viewBox="0 0 20 17"><rect x="5" y="0" width="10" height="5" fill="#555"/><rect x="0" y="5" width="20" height="8" rx="1" fill="#555"/><rect x="5" y="10" width="10" height="7" fill="#555" stroke="#fff" stroke-width="1"/></svg>Print</span>
      <span><svg width="17" height="17" viewBox="0 0 17 17"><rect width="17" height="17" rx="2" fill="#555"/><path d="M4 4l4.5 4L13 4M4 9l4.5 4L13 9" stroke="#fff" stroke-width="1.8" fill="none"/></svg>Download</span>
    </div>

    <table class="student-table">
      <colgroup>
        <col style="width:56px"><col style="width:89px"><col style="width:69px"><col style="width:103px">
        <col style="width:95px"><col style="width:99px"><col style="width:134px"><col style="width:119px">
        <col style="width:57px"><col style="width:114px"><col style="width:83px"><col style="width:76px"><col style="width:63px">
      </colgroup>
      <thead>
        <tr><th>Date</th><th>Grade</th><th>ESC</th><th>CDC#</th><th>District</th><th>Capus</th><th>Last Name</th><th>First Name</th><th>MI</th><th>Student ID</th><th>Genter</th><th>DOB</th><th>Hisp</th></tr>
      </thead>
      <tbody>
        <tr><td class="center">411</td><td class="center">9</td><td>10</td><td>999999001</td><td>Example</td><td>Example HS</td><td>Accountability</td><td>Nathalie</td><td></td><td>630543340</td><td class="center">F</td><td>7311996</td><td>1</td></tr>
        <tr><td class="center">411</td><td class="center">9</td><td>10</td><td>999999001</td><td>Example</td><td>Example HS</td><td>Accountability</td><td>Nathalie</td><td></td><td>630543340</td><td class="center">F</td><td>7311996</td><td>1</td></tr>
        <tr><td class="center">411</td><td class="center">9</td><td>10</td><td>999999001</td><td>Example</td><td>Example HS</td><td>Accountability</td><td>Nathalie</td><td></td><td>630543340</td><td class="center">F</td><td>7311996</td><td>1</td></tr>
        <tr><td class="center">411</td><td class="center">9</td><td>10</td><td>999999001</td><td>Example</td><td>Example HS</td><td>Accountability</td><td>Nathalie</td><td></td><td>630543340</td><td class="center">F</td><td>7311996</td><td>1</td></tr>
        <tr><td class="center">411</td><td class="center">9</td><td>10</td><td>999999001</td><td>Example</td><td>Example HS</td><td>Accountability</td><td>Nathalie</td><td></td><td>630543340</td><td class="center">F</td><td>7311996</td><td>1</td></tr>
        <tr><td class="center">411</td><td class="center">9</td><td>10</td><td>999999001</td><td>Example</td><td>Example HS</td><td>Accountability</td><td>Nathalie</td><td></td><td>630543340</td><td class="center">F</td><td>7311996</td><td>1</td></tr>
        <tr><td class="center">411</td><td class="center">9</td><td>10</td><td>999999001</td><td>Example</td><td>Example HS</td><td>Accountability</td><td>Nathalie</td><td></td><td>630543340</td><td class="center">F</td><td>7311996</td><td>1</td></tr>
        <tr><td class="center">411</td><td class="center">9</td><td>10</td><td>999999001</td><td>Example</td><td>Example HS</td><td>Accountability</td><td>Nathalie</td><td></td><td>630543340</td><td class="center">F</td><td>7311996</td><td>1</td></tr>
        <tr><td class="center">411</td><td class="center">9</td><td>10</td><td>999999001</td><td>Example</td><td>Example HS</td><td>Accountability</td><td>Nathalie</td><td></td><td>630543340</td><td class="center">F</td><td>7311996</td><td>1</td></tr>
        <tr><td class="center">411</td><td class="center">9</td><td>10</td><td>999999001</td><td>Example</td><td>Example HS</td><td>Accountability</td><td>Nathalie</td><td></td><td>630543340</td><td class="center">F</td><td>7311996</td><td>1</td></tr>
      </tbody>
    </table>

    <div class="pager-row bottom">
      <div class="pager">
        <span class="page"><svg width="7" height="10" viewBox="0 0 7 10"><path d="M6 1 2 5l4 4" stroke="#444" stroke-width="1.6" fill="none"/></svg></span>
        <span class="page">1</span><span class="page">2</span><span class="page">3</span>
        <span class="page is-current">4</span><span class="page">5</span>
        <span class="ellipsis">...</span>
        <span class="page">10</span><span class="page">20</span><span class="page">30</span>
        <span class="page"><svg width="7" height="10" viewBox="0 0 7 10"><path d="M1 1l4 4-4 4" stroke="#444" stroke-width="1.6" fill="none"/></svg></span>
      </div>
      <span>Show</span>
      <span class="rows-select">10<svg width="9" height="6" viewBox="0 0 9 6"><path d="M1 1l3.5 3.5L8 1" stroke="#555" stroke-width="1.5" fill="none"/></svg></span>
      <span>rows &nbsp;per page</span>
    </div>
  </main>
</body>
</html>
```